Business Card design

Keen on a very modern design with using the red star as a feature point preferably will have it printed with red foiling.

Target Market(s)

Cosmetics

Industry/Entity Type

Cosmetics

Contact Information for Business Card

Marnie Telford
Director
17 Brisbrook Lane
Wyndale Heights Calder
Eastland 4821
marnie@glowcratesupply.com.au

Font styles to use
Sans Serif

Colors
ec1f27
000000

Requirements
Must have
• Keen on some red stars on back with black background and I may get the red components printed as red foiling potentially

```html
<!DOCTYPE html>
<html lang="en">
<head>
<meta charset="utf-8">
<title>Marnie Telford – Business Card</title>
<link rel="stylesheet" href="https://fonts.googleapis.com/css2?family=Cabin+Condensed:wght@400;600&display=swap">
<style>
  :root {
    --card-black: #000000;
    --foil-red: #ec1f27;
    --paper-white: #ffffff;
  }
  html, body {
    margin: 0;
    padding: 0;
    overflow: hidden;
    background: var(--paper-white);
  }
  .card {
    position: relative;
    width: 1186px;
    height: 1200px;
    background: var(--paper-white);
    font-family: "Cabin Condensed", sans-serif;
    overflow: hidden;
  }
  .card__badge {
    position: absolute;
    inset: 0;
    width: 1186px;
    height: 1200px;
  }
  .badge-shape { fill: var(--card-black); }
  .divider { fill: var(--paper-white); }
  .foil-star { fill: var(--foil-red); }

  .card__email {
    position: absolute;
    left: 350px;
    top: 40px;
    height: 990px;
    writing-mode: vertical-rl;
    transform: rotate(180deg);
    text-align: start;
    color: var(--paper-white);
    font-size: 62px;
    font-weight: 400;
    line-height: 72px;
    white-space: nowrap;
  }
  .card__details {
    position: absolute;
    left: 494px;
    top: 180px;
    margin: 0;
    padding: 0;
    list-style: none;
    color: var(--paper-white);
    font-size: 68px;
    font-weight: 600;
    line-height: 134px;
    white-space: nowrap;
  }
</style>
</head>
<body>
  <div class="card">
    <svg class="card__badge" viewBox="0 0 1186 1200" aria-hidden="true">
      <path class="badge-shape" d="
        M593,6
        C703,6 740.7,60.4 805.4,87.2
        C870.1,114 964.9,72.5 1042.7,150.3
        C1120.5,228.1 1079,322.9 1105.8,387.6
        C1132.6,452.3 1178,490 1178,600
        C1178,710 1132.6,747.7 1105.8,812.4
        C1079,877.1 1120.5,971.9 1042.7,1049.7
        C964.9,1127.5 870.1,1086 805.4,1112.8
        C740.7,1139.6 703,1194 593,1194
        C483,1194 445.3,1139.6 380.6,1112.8
        C315.9,1086 221.1,1127.5 143.3,1049.7
        C65.5,971.9 107,877.1 80.2,812.4
        C53.4,747.7 8,710 8,600
        C8,490 53.4,452.3 80.2,387.6
        C107,322.9 65.5,228.1 143.3,150.3
        C221.1,72.5 315.9,114 380.6,87.2
        C445.3,60.4 483,6 593,6 Z"/>
      <rect class="divider" x="463" y="40" width="6" height="1100"/>
      <polygon class="foil-star" transform="translate(590 1020) rotate(6) scale(1.05)"
        points="0,-76 17,-23.5 72.3,-23.5 27.6,9 44.7,61.5 0,29 -44.7,61.5 -27.6,9 -72.3,-23.5 -17,-23.5"/>
    </svg>

    <div class="card__email">marnie@glowcratesupply.com.au</div>

    <ul class="card__details">
      <li class="card__name">Marnie Telford</li>
      <li class="card__title">Director</li>
      <li class="card__street">17 Brisbrook Lane</li>
      <li class="card__suburb">Wyndale Heights Calder</li>
      <li class="card__country">Eastland 4821</li>
    </ul>
  </div>
</body>
</html>
```